Vertical Mini Totem Poster for Velmora Day Pass

Overview
We are looking for a visually striking vertical mini totem-style public signage design to promote the Day Pass at Velmora Beach & Jungle Resort, located in front of Playa Cocles in Costa Rica. The design should be tropical, relaxed, and attractive to tourists and day visitors.
Design Objective
Create a clean and impactful design with five horizontal sections, each with a specific message. It must be easy to read from a distance and aligned with the Velmora brand identity.
Final Format & Specifications
Artwork Size: 123 cm (width) x 157.5 cm (height)
Divisions: 5 horizontal bands of 123 cm x 31.5 cm each
Orientation: Vertical
Resolution: 300 DPI
Color Mode: CMYK
Final File Format: Editable AI or PDF
Images: Embedded in high resolution
Text & Logos: Outlined
Safe Zones: Keep critical text away from borders and cut lines
We are attaching:
A detailed technical specification sheet of the totem structure where this design will be printed
An Illustrator template to guide your design layout
Content Breakdown (Top to Bottom)
Top Band: Velmora logo – must be clearly visible but not larger than the “Day Pass” title
Second Band: Main text – “Day Pass” – this should be the biggest and most eye-catching element
Third Band: Secondary message – “Pool, wetbar & restaurant”
Fourth Band: Extra info – “In front of Playa Cocles / From 11:00 a.m. to 6:00 p.m.”
Bottom Band: Social media & contact – WhatsApp + Instagram icons, handle @velmorahotel, number +506 84207352
Design Style
Font Family: Avenir (preferably Black, Heavy, or Bold for hierarchy)
Brand Colors:
Blue: #406EA7
Fuchsia: #F62188
Light Blue: #DFECFD
Use white and black for contrast and readability if needed
Background Image
We will provide several high-resolution photos of our pool, wetbar, or hotel areas. You may use one as a full background or integrate it into the design. Filters or gradient overlays can be used to ensure text visibility.
Creative Input
We’re open to smart layout adjustments, iconography, or other enhancements to improve clarity and visual appeal. Just ensure the 5-band structure is maintained and readable.

```html
<!DOCTYPE html>
<html lang="en">
<head>
<meta charset="utf-8">
<title>Velmora Day Pass Totem</title>
<link href="https://fonts.googleapis.com/css2?family=Nunito+Sans:wght@400;600;700;800;900&display=swap" rel="stylesheet">
<style>
  :root{
    --blue:#406EA7;
    --fuchsia:#F62188;
    --light-blue:#DFECFD;
    --white:#ffffff;
    --black:#000000;
    --road-green:#00753A;
    --ground-top:#ffffff;
    --ground-bottom:#b2b2b2;
  }
  *{margin:0;padding:0;box-sizing:border-box}
  html,body{width:1032px;height:1200px;overflow:hidden}
  body{
    position:relative;
    font-family:"Nunito Sans",sans-serif;
    background:linear-gradient(to bottom,var(--ground-top) 0%,var(--ground-top) 30%,#eef4fd 45%,#d6dbe2 70%,var(--ground-bottom) 100%);
  }
  .post{position:absolute;top:72px;width:25px;height:1076px;background:var(--black)}
  .post--left{left:298px}
  .post--right{left:714px}

  .band{position:absolute;left:198px;width:636px;height:163px;overflow:hidden}
  .band--logo{top:73px;background:var(--blue)}
  .band--title{top:249px}
  .band--offer{top:425px}
  .band--info{top:601px}
  .band--contact{top:777px;background:var(--light-blue)}

  .photo{position:absolute;inset:0}
  .photo--pool{
    left:358px;top:0;width:290px;height:163px;border-radius:50% 0 0 50% / 50% 0 0 50%;
    background:radial-gradient(ellipse at 55% 55%,#4f9be0 0%,#7fb8e6 22%,#e8d8c8 38%,#5f8e3e 62%,#3d6b2a 100%);
    box-shadow:-8px 0 0 0 var(--light-blue);
  }
  .photo--terrace{background:linear-gradient(100deg,#3d5a3a 0%,#6a7f5c 30%,#b48a6e 55%,#c9b7aa 75%,#e6e9ec 100%)}
  .photo--guest{background:linear-gradient(90deg,#d9dde0 0%,#8a6a55 15%,#c79c80 35%,#e6b4a4 55%,#f0c6cf 100%)}
  .photo--drink{background:linear-gradient(90deg,#d9dde4 0%,#a9b5c6 25%,#f0e27a 45%,#d9c9b8 65%,#6b86b6 100%)}
  .photo--shirt{left:0;width:300px;background:linear-gradient(90deg,#e7e9ee 0%,#b9c3cf 50%,#dfe4ea 100%)}

  .logo{position:absolute;left:89px;top:44px;width:210px;text-align:center;color:var(--light-blue)}
  .logo__name{font-size:50px;font-weight:800;line-height:1}
  .logo__tagline{margin-top:8px;font-size:8.5px;font-weight:600;letter-spacing:2px}

  .title{
    position:absolute;left:74px;top:22px;font-size:98px;font-weight:900;line-height:1;
    color:var(--fuchsia);letter-spacing:-3px;white-space:nowrap;text-shadow:3px 3px 0 #3a1020;
  }
  .title__rule{position:absolute;left:35px;top:124px;width:566px;height:5px;background:var(--fuchsia)}

  .offer__panel{position:absolute;left:250px;top:0;width:386px;height:163px;background:linear-gradient(90deg,rgba(246,33,136,0) 0%,rgba(246,33,136,.85) 25%,var(--fuchsia) 45%)}
  .offer__pool{
    position:absolute;right:26px;top:28px;font-size:60px;font-weight:900;line-height:1;
    color:var(--white);text-shadow:-3px 3px 0 var(--black);
  }
  .offer__sub{
    position:absolute;left:375px;top:100px;width:261px;height:31px;background:var(--white);
    color:var(--fuchsia);font-size:17px;font-weight:800;text-align:right;padding-right:26px;
    line-height:31px;white-space:nowrap;
  }

  .info__shapes{position:absolute;inset:0}
  .info__lead{position:absolute;right:26px;top:66px;font-size:17px;font-weight:600;color:var(--white);border-top:1.5px solid var(--light-blue);padding-left:90px;line-height:1.3}
  .info__place{position:absolute;right:26px;top:90px;font-size:28px;font-weight:800;color:var(--fuchsia);text-shadow:-1.5px 1.5px 0 var(--black);line-height:1}
  .info__hours{position:absolute;right:26px;top:124px;font-size:29px;font-weight:800;color:var(--white);line-height:1;white-space:nowrap}

  .contact__line{position:absolute;right:26px;font-weight:600;color:var(--black);border-bottom:1.5px solid var(--black);text-align:right;line-height:1.2;white-space:nowrap}
  .contact__phone{top:40px;font-size:26px;padding-left:8px}
  .contact__handle{top:114px;font-size:20px;padding-left:20px}
  .contact__icon{position:absolute;right:27px}
  .contact__icon--phone{top:15px}
  .contact__icon--social{top:92px}

  .road-sign{position:absolute;left:198px;top:953px;width:636px;height:142px;background:var(--road-green)}
  .road-sign__arrow{position:absolute;left:46px;top:30px}
  .road-sign__label{position:absolute;left:211px;top:34px;font-size:58px;font-weight:800;color:var(--white);line-height:1;letter-spacing:1px}
</style>
</head>
<body>
  <div class="post post--left"></div>
  <div class="post post--right"></div>

  <section class="band band--logo">
    <div class="logo">
      <div class="logo__name">Velmora</div>
      <div class="logo__tagline">BEACH &amp; JUNGLE RESORT</div>
    </div>
    <div class="photo photo--pool" role="img" aria-label="Aerial view of the resort pool surrounded by umbrellas and tropical garden"></div>
  </section>

  <section class="band band--title">
    <div class="photo photo--terrace" role="img" aria-label="Smiling guest in sunglasses on a sunny poolside terrace"></div>
    <h1 class="title">DAY PASS</h1>
    <div class="title__rule"></div>
  </section>

  <section class="band band--offer">
    <div class="photo photo--guest" role="img" aria-label="Young boy with a tropical drink at the pool bar"></div>
    <div class="offer__panel"></div>
    <div class="offer__pool">POOL</div>
    <div class="offer__sub">WETBAR &amp; RESTAURANT</div>
  </section>

  <section class="band band--info">
    <div class="photo photo--drink" role="img" aria-label="Boy holding a pineapple smoothie beside a table of fresh fruit"></div>
    <svg class="info__shapes" width="636" height="163" viewBox="0 0 636 163" aria-hidden="true">
      <polygon points="0,119 180,119 130,163 0,163" fill="#F62188"/>
      <polygon points="395,0 636,0 636,163 160,163 210,119 395,119" fill="#406EA7" opacity="0.92"/>
    </svg>
    <div class="info__lead">IN FRONT OF</div>
    <div class="info__place">PLAYA COCLES</div>
    <div class="info__hours">FROM 11:00 A.M. TO 6:00 P.M.</div>
  </section>

  <section class="band band--contact">
    <div class="photo photo--shirt" role="img" aria-label="Boy in a tropical print shirt holding a smoothie glass"></div>
    <svg class="contact__icon contact__icon--phone" width="28" height="28" viewBox="0 0 28 28" aria-hidden="true">
      <circle cx="14" cy="14" r="13" fill="#406EA7"/>
      <path d="M10 7.5c.6-.3 1.3-.1 1.6.5l1.2 2.3c.3.5.1 1.1-.3 1.4l-1 .8c.7 1.6 1.9 2.8 3.5 3.5l.8-1c.3-.4.9-.6 1.4-.3l2.3 1.2c.6.3.8 1 .5 1.6l-.6 1.1c-.4.7-1.2 1.1-2 .9-4.2-1-7.5-4.3-8.5-8.5-.2-.8.2-1.6.9-2z" fill="#ffffff"/>
    </svg>
    <div class="contact__line contact__phone">+506 84207352</div>
    <svg class="contact__icon contact__icon--social" width="24" height="24" viewBox="0 0 24 24" aria-hidden="true">
      <rect x="0" y="0" width="24" height="24" rx="5" fill="#F62188"/>
    </svg>
    <div class="contact__line contact__handle">handle @velmorahotel</div>
  </section>

  <div class="road-sign">
    <svg class="road-sign__arrow" width="50" height="90" viewBox="0 0 50 90" aria-hidden="true">
      <path d="M4 0 L34 4 L24 12 C38 22 45 32 45 48 L45 88 L24 88 L24 50 C24 40 20 32 12 26 L6 34 Z" fill="#ffffff"/>
    </svg>
    <div class="road-sign__label">SAN JOSÉ</div>
  </div>
</body>
</html>
```